Dr. Marissa Tevlin Medical/Chiropractic Business Card

Dr. Tevlin is a chiropractor and will require a business card that she uses every single day to book appointments on the back side of the card. Currently the office name goes by Dr. Marissa Tevlin. The chiropractic profession is based on the diagnosis and manipulative treatment of misalignments of the joints, especially those of the spinal column, which are held to cause other disorders by affecting the nerves, muscles, and organs. Dr. Marissa Tevlin is looking for a contemporary and minimalistic design.

Industry/Entity Type

Medical

Contact Information for Business Card

Name: Dr. Marissa Tevlin; Address: 748 Harcastle Rd South, London, ON N5R 2K7; Phone Number: 519.274.6193; Fax: 519.281.5046; email: marissa.tevlin@quorvamail.com

Requirements
Must have
• ability to write multiple appointments date/time on the back of card

```html
<!DOCTYPE html>
<html lang="en">
<head>
<meta charset="utf-8">
<title>Dr. Marissa Tevlin – Business Card</title>
<link rel="stylesheet" href="https://fonts.googleapis.com/css2?family=Montserrat:wght@400;500;600;700;800&display=swap">
<style>
  :root {
    --bg: #e9ebee;
    --card: #ffffff;
    --blue: #1e82c8;
    --blue-line: #3d95d3;
    --red: #dc1f28;
    --ink-blue: #1e82c8;
    --shadow: 0 10px 30px rgba(20, 30, 50, 0.18);
  }
  * { box-sizing: border-box; margin: 0; padding: 0; }
  html, body {
    width: 1200px; height: 900px; overflow: hidden;
    background: var(--bg);
    font-family: "Montserrat", Arial, sans-serif;
  }
  .stage {
    width: 1200px; height: 900px;
    display: flex; flex-direction: column; align-items: center; justify-content: center;
    gap: 56px;
  }
  .card {
    position: relative;
    width: 630px; height: 360px;
    background: var(--card);
    box-shadow: var(--shadow);
    overflow: hidden;
  }

  /* ---------- Appointment side ---------- */
  .time-band {
    position: absolute; left: 380px; right: 0; top: 20px; height: 24px;
    background: var(--blue);
    color: #fff; font-weight: 700; font-size: 13px; letter-spacing: 0.5px;
    padding-left: 82px; line-height: 24px;
  }
  .title-pill {
    position: absolute; left: 150px; top: 26px; width: 240px; height: 40px;
    background: var(--red); border-radius: 20px;
    color: #fff; font-weight: 700; font-size: 19px; letter-spacing: 1.2px;
    display: flex; align-items: center; justify-content: center;
  }
  .date-band {
    position: absolute; left: 0; width: 390px; top: 66px; height: 24px;
    background: var(--blue);
    color: #fff; font-weight: 700; font-size: 13px; letter-spacing: 0.5px;
    padding-left: 178px; line-height: 24px;
  }
  .ruled-grid { position: absolute; left: 0; top: 0; }
  .notice-band {
    position: absolute; left: 0; right: 0; bottom: 0; height: 62px;
    background: var(--red);
    color: #fff; font-size: 13px; font-weight: 500; line-height: 18px;
    text-align: center; padding-top: 13px; padding-left: 180px;
  }

  /* ---------- Identity side ---------- */
  .wave { position: absolute; left: 0; top: 0; }
  .identity {
    position: absolute; right: 296px; top: 122px; text-align: right;
  }
  .identity .name {
    color: var(--red); font-weight: 800; font-size: 22px; letter-spacing: 0.2px; white-space: nowrap;
  }
  .identity .role {
    color: var(--ink-blue); font-weight: 500; font-size: 14px; letter-spacing: 0.8px; margin-top: 2px;
  }
  .divider {
    position: absolute; left: 346px; top: 86px; width: 3px; height: 124px; background: var(--blue);
  }
  .contacts {
    position: absolute; left: 362px; top: 84px;
    list-style: none; color: var(--ink-blue); font-size: 13px; font-weight: 500; line-height: 19px;
    white-space: nowrap;
  }
  .contacts li { display: flex; align-items: center; gap: 8px; }
  .contacts .icon { width: 11px; height: 11px; flex: none; }
  .contacts .address { display: block; padding-left: 19px; margin-top: 4px; }
</style>
</head>
<body>
<main class="stage">

  <!-- Appointment side -->
  <section class="card card-appointments" aria-label="Appointment card">
    <svg class="ruled-grid" width="630" height="360" viewBox="0 0 630 360" aria-hidden="true">
      <g stroke="var(--blue-line)" stroke-width="1.2">
        <line x1="0" y1="114" x2="630" y2="114"/>
        <line x1="0" y1="138" x2="630" y2="138"/>
        <line x1="0" y1="162" x2="630" y2="162"/>
        <line x1="0" y1="186" x2="630" y2="186"/>
        <line x1="0" y1="210" x2="630" y2="210"/>
        <line x1="0" y1="234" x2="630" y2="234"/>
        <line x1="0" y1="258" x2="630" y2="258"/>
        <line x1="0" y1="282" x2="630" y2="282"/>
        <line x1="390" y1="68" x2="630" y2="68"/>
        <line x1="390" y1="90" x2="630" y2="90"/>
      </g>
      <line x1="390" y1="44" x2="390" y2="298" stroke="var(--red)" stroke-width="1.5"/>
    </svg>
    <div class="time-band">TIME</div>
    <div class="date-band">DATE</div>
    <div class="title-pill">APPOINTMENTS</div>
    <p class="notice-band">If you are unable to make your appointment,<br>please call us to reschedule</p>
  </section>

  <!-- Identity side -->
  <section class="card card-identity" aria-label="Business card front">
    <svg class="wave" width="630" height="360" viewBox="0 0 630 360" aria-hidden="true">
      <path d="M0 360 L0 335 C120 255 300 250 430 225 C520 205 585 170 630 128 L630 360 Z" fill="var(--blue)"/>
      <path d="M40 318 C150 262 300 252 430 232 C520 214 585 180 630 140 L630 150 C585 192 520 226 430 244 C300 266 150 276 40 318 Z" fill="#fff"/>
      <path d="M150 300 C260 270 380 265 470 245 C540 228 590 200 620 178" fill="none" stroke="#fff" stroke-width="2"/>
    </svg>

    <div class="identity">
      <h1 class="name">DR. MARISSA TEVLIN</h1>
      <p class="role">CHIROPRACTOR</p>
    </div>
    <div class="divider"></div>

    <ul class="contacts">
      <li>
        <svg class="icon" viewBox="0 0 12 12" aria-hidden="true"><path d="M2.3 0.8 L4.3 2.9 L3.3 4.4 C4 6 5.5 7.6 7.2 8.5 L8.6 7.5 L11 9.5 L9.8 11.2 C5.3 11 0.9 6.6 0.7 2 Z" fill="var(--red)"/></svg>
        519.274.6193
      </li>
      <li>
        <svg class="icon" viewBox="0 0 12 12" aria-hidden="true"><rect x="3" y="0.8" width="6" height="3" fill="var(--red)"/><rect x="0.8" y="4.3" width="10.4" height="4.4" rx="1" fill="var(--red)"/><rect x="3" y="8" width="6" height="3.4" fill="var(--red)"/></svg>
        519.281.5046
      </li>
      <li>
        <svg class="icon" viewBox="0 0 12 12" aria-hidden="true"><rect x="0.8" y="2.2" width="10.4" height="7.6" fill="none" stroke="var(--red)" stroke-width="1.3"/><path d="M0.8 2.4 L6 6.6 L11.2 2.4" fill="none" stroke="var(--red)" stroke-width="1.3"/></svg>
        marissa.tevlin@quorvamail.com
      </li>
      <li class="address">748 Harcastle Rd South,<br>London, ON N5R 2K7</li>
    </ul>
  </section>

</main>
</body>
</html>
```